Yoga/movement guide/teacher for adult yoga practice and kid yoga

What is the positioning or mission statement of your company? to guide individuals in a yoga-based safe and sustainable movement practice applicable to all ages and body types. Currently my focus is working with children in daycare and school settings, but my goal is to expand into private yoga practice for adults, and potentially as part of rented space in studios. I hope to find a way to work with children AND adults (so would love for logo to be appealing to both), but current focus is with children based on need and demand in the community. yoga for children also compliments my backround as a pediatrician/neonatologist, and I greatly miss interacting with children. I also want to emphasize a yoga/movement practice that is focused more on what one feels internally through movement. NOT what one looks like asthetically. I believe in removing all mirrors from yoga/movement practice. It should be an experience of movement/poses/yoga through appropriate cueing and education. It is not about the details of how far the knee should bend, or how high the leg should be. Focusing on foudation first, core, then core engagement and ultimately expression of poses/movements. A focus on strength, stability and mobility, not just flexibility, which is the common perception/association with yoga. I also want individuals to learn to be an advocate of their own health. Through guidance, I hope for individuals to connect with their body so they know themselves so well to be able to advocate for themselves in the modern healthcare world. This internal experience and connection is so essential in a world where modern medicine has become a business and it is all about making a dollar. the connection with patients is lost, and individuals need to learn to empower themselves and through their new found voice to be able to articulate what is wrong.<br/>Does your company have a tagline or slogan that should be included with the logo? "Practice Glowing Motion"<br/>What do you hope your company can be known for? Accessible yoga for a sustained practice. A guided movement practice where one gains information and knowledge of oneself through a mind/body connection. For one feel good physically with a new awaraness of their internal radiance that exists in all beings. Physical rejuvenation egnites a light and increases energy to flow through the physical body, which ultimately tranlates into works of kindness for others and out in the world. <br/>What color palettes might you prefer? why? love the colors currently chosen<br/>Where will the logo be primarily used? initially business cards, but hopefully future websites, t-shirts, and potentially local magazine adds. Also starting with a small couple of banners for community events in the area. I currently practice as a nomad out of my car :)<br/>Are there any elements you would prefer to see in the logo? Movement. A modern depiction of a human body/figure practicing movement. Hoping to avoid a stereotypical yoga pose per say, just because I want to people to think of it more of a movement practice with yoga roots. Modern yoga. There are elements of breathing and connecting with oneself through the flow of breath and movement, but I do not focus on the meditative/cerebral aspect of the yoga practice. What I teach is almost reaching a meditative state through movement. I personally don't practice, nor resonate with just seated meditation. just not my thing :)<br/>In your opinion, what defines a well-designed logo? curiosity. enough info for individuals to think they know what it means, but want to know more. invokes curiosity, but not too abstract. Reproducible. not too complicated. I want also to invoke a community feel, so a design that appeals to all people within a community. <br/>What is your preference in reference to icons, typography, spokespeople (characters), etc.? modern design. I love the idea of a logo for my purposes, to invoke a sense of movement from within. So not too static. <br/>What words or icons must be included in the logo? movement with yoga roots. <br/>What logos do you like and why? A representation, but not exact. I think some ambiguity is intriguing for others, and also memorable. I want it to be an artistic representation of movement/yoga<br/>What logos do you dislike and why? too busy, too loud. <br/>In your opinion, what is the primary purpose for a logo? association<br/>Who is the primary target audience? (who is most likely to use your services/product?) Children and their parents, but ultimately to expand into teaching adults. I even have aspirations of prenatal and post-natal yoga. Potentially incorporating infants. <br/>Who currently uses your product the most? n/a (working in schools/daycare currently. It is currently all volunteer)<br/>Are you pleased with the range of people your company serves? n/a<br/>Are you looking to expand, modify, or completely change your target audience? or will it remain the same? yes! expand into an adult audience. <br/>How do you plan to focus on your target audience? currently by working through schools and daycares. hopefully ultimately through after school care programs and then offering kid yoga in an existing yoga studio (working on this with Q Loft in Ridgeland, currently)<br/>What are your main forms of advertising? word of mouth, schools, daycares. Happy kids talking to their parents about the yoga class they took and happy teachers :)<br/>How do most customers find out about your company?<br/>Which gender are you targeting? All genders! However, with kid yoga, often the maternal individual in the child's life is more involved with decision making as far as extracurricular activities

Target Market(s)

individuals and families interested in wellness and feeling great

Contact Information for Business Card

Dana Whitmore
Yoga Instructor
RYT-200, RCYT

certified yoga teacher for adults and children

Colors

Designer to choose colors to be used in the design.

Requirements
Must have
• "Practice Glowing Motion"
Nice to have
• logo with same colors

```html
<!DOCTYPE html>
<html lang="en">
<head>
<meta charset="UTF-8">
<title>Daybreak Studios — Business Card</title>
<link rel="stylesheet" href="https://fonts.googleapis.com/css2?family=Open+Sans:wght@300;400;700&family=Josefin+Sans:wght@300&display=swap">
<style>
  :root {
    --backdrop: #d6d6d6;
    --card-grey: #bdbec0;
    --card-white: #ffffff;
    --sun-yellow: #fddf4f;
    --aqua: #5ecbd0;
    --ink-grey: #6d6e70;
    --shadow: rgba(0, 0, 0, 0.28);
  }
  * { box-sizing: border-box; margin: 0; padding: 0; }
  html, body {
    width: 1200px; height: 900px; overflow: hidden;
    background: var(--backdrop);
    font-family: "Open Sans", Arial, sans-serif;
  }
  .stage { position: relative; width: 1200px; height: 900px; }

  .card {
    position: absolute;
    width: 520px; height: 298px;
    box-shadow: 0 6px 14px var(--shadow);
    overflow: hidden;
  }

  /* Back of card */
  .card--back { left: 90px; top: 150px; background: var(--card-grey); }
  .back-mark__dot {
    position: absolute; left: 30px; top: 120px;
    width: 150px; height: 150px; border-radius: 50%;
    background: var(--sun-yellow);
  }
  .back-mark__name {
    position: absolute; left: 196px; top: 168px;
    font-weight: 700; font-size: 24px; color: var(--card-white);
    line-height: 1.1; white-space: nowrap;
  }
  .swirl {
    position: absolute; border-radius: 50%;
    background: var(--sun-yellow);
  }
  .swirl--top { width: 62px; height: 62px; right: 60px; top: 14px; }
  .swirl--edge { width: 120px; height: 120px; right: -30px; top: 150px; }
  .swirl--small-a { width: 26px; height: 26px; left: 290px; top: 58px; }
  .swirl--small-b { width: 22px; height: 22px; left: 362px; top: 160px; }
  .swirl--small-c { width: 34px; height: 34px; left: 300px; top: 240px; }
  .back-tagline {
    position: absolute; left: 180px; top: 100px;
    font-family: "Josefin Sans", "Open Sans", sans-serif;
    font-weight: 300; font-size: 13px; letter-spacing: 3px;
    text-transform: uppercase; color: var(--card-white);
    white-space: nowrap;
  }

  /* Front of card */
  .card--front { left: 590px; top: 440px; background: var(--card-white); }
  .front-logo {
    position: absolute; left: 34px; top: 120px;
    display: flex; align-items: center; gap: 12px;
  }
  .front-logo__dot {
    width: 90px; height: 90px; border-radius: 50%;
    background: var(--sun-yellow);
  }
  .front-logo__name {
    font-weight: 300; font-size: 26px; color: var(--ink-grey);
    line-height: 1.05;
  }
  .front-tagline {
    position: absolute; left: 140px; top: 200px;
    font-size: 7px; letter-spacing: 2px; text-transform: uppercase;
    color: var(--aqua); white-space: nowrap;
  }
  .contact {
    position: absolute; left: 300px; top: 58px;
  }
  .contact__name { font-weight: 700; font-size: 20px; color: var(--aqua); }
  .contact__role { font-size: 14px; color: var(--ink-grey); margin-top: 2px; }
  .contact__rule {
    width: 38px; height: 3px; background: var(--sun-yellow);
    margin: 18px 0 16px;
  }
  .contact__list { list-style: none; }
  .contact__item {
    display: flex; align-items: center; gap: 8px;
    font-size: 12.5px; color: var(--ink-grey); line-height: 1.6;
    white-space: nowrap;
  }
  .contact__item svg { width: 12px; height: 12px; flex: none; }
</style>
</head>
<body>
<main class="stage">

  <section class="card card--back" aria-label="Card back">
    <span class="back-mark__dot"></span>
    <span class="back-mark__name">Daybreak<br>Studios</span>
    <span class="swirl swirl--top" role="img" aria-label="Hand-drawn yellow swirl ornament"></span>
    <span class="swirl swirl--edge" role="img" aria-label="Large yellow swirl ornament at card edge"></span>
    <span class="swirl swirl--small-a" role="img" aria-label="Small yellow swirl ornament"></span>
    <span class="swirl swirl--small-b" role="img" aria-label="Small yellow swirl ornament"></span>
    <span class="swirl swirl--small-c" role="img" aria-label="Small yellow swirl ornament"></span>
    <p class="back-tagline">Practice Glowing Motion</p>
  </section>

  <section class="card card--front" aria-label="Card front">
    <div class="front-logo">
      <span class="front-logo__dot"></span>
      <span class="front-logo__name">Daybreak<br>Studios</span>
    </div>
    <p class="front-tagline">Practice Glowing Motion</p>

    <div class="contact">
      <h1 class="contact__name">Rowan Ellis</h1>
      <p class="contact__role">Founder</p>
      <div class="contact__rule"></div>
      <ul class="contact__list">
        <li class="contact__item">
          <svg viewBox="0 0 12 12" aria-hidden="true"><path d="M3 1 L5 3.5 L4 5 Q5 7 7 8 L8.5 7 L11 9 L9.5 11 Q4 10.5 1 2.5 Z" fill="var(--aqua)"/></svg>
          555-014-2290
        </li>
        <li class="contact__item">
          <svg viewBox="0 0 12 12" aria-hidden="true"><rect x="1" y="2.5" width="10" height="7" fill="none" stroke="var(--aqua)" stroke-width="1.3"/><path d="M1 2.5 L6 6.5 L11 2.5" fill="none" stroke="var(--aqua)" stroke-width="1.3"/></svg>
          danawhitmore@mail.com
        </li>
        <li class="contact__item">
          <svg viewBox="0 0 12 12" aria-hidden="true"><circle cx="6" cy="6" r="5" fill="none" stroke="var(--aqua)" stroke-width="1.2"/><path d="M1 6 H11 M6 1 Q3 6 6 11 M6 1 Q9 6 6 11" fill="none" stroke="var(--aqua)" stroke-width="1"/></svg>
          www.daybreakstudios.com
        </li>
      </ul>
    </div>
  </section>

</main>
</body>
</html>
```